Bright Acorn day Nursery flyer

I need a great flyer to attract new parents. Bright Acorn Is a fantastic, warm and homely nursery in Hazelmere road SE6 London. We offer many things that other nurseries don't offer such as Spanish, Yoga, Music, Cooking classes and Handsign. We also have an amazing system called KIDTRAK that allows parents to get alerts on the KIDTRAK app about their children daily activities and even developmental reports. Parents are able to share with the nursery great moments and put pictures and videos through the app. We also offer the parent camera, an extremely safe system that allows parents to log in and see their children whilst they are engaged in exciting activities.
Full details of Nursery
87 Hazelmere road
SE6 4PW
02084417263
www.brightacornwexley.co.uk
facebook page
brightacorndaynursery@brightacornwexley.co.uk
Updates

double sided or mini brochure type

Hi Please keep it simple and clean I feel the designs are a good attempt thank you but they are very busy and I just want to add important points a lot of the designs have too many colours, too much text etc Thank you!

https://www.facebook.com/brightacornwexley.co.uk/

Target Market(s)

parents of children 0-5

Industry/Entity Type

Childcare

Colors

Designer to choose colors to be used in the design.

Requirements
Must have
• colour and pictures but clean design

```html
<!DOCTYPE html>
<html lang="en">
<head>
<meta charset="utf-8">
<title>Bright Acorn Day Nursery – Flyer</title>
<link rel="stylesheet" href="https://fonts.googleapis.com/css2?family=Itim&family=PT+Sans:wght@400;700&family=Caveat:wght@600&display=swap">
<style>
:root{
  --bg:#e7e5e2;
  --cream:#fbf8ef;
  --teal:#17a898;
  --teal-line:#3cb8ab;
  --pink:#f1a2b4;
  --pink-soft:#f6c9d3;
  --navy:#3e59a5;
  --activity:#3a4fa6;
  --body:#5a5a5a;
  --white:#ffffff;
  --peg:#c9a27a;
  --string:#8a5a3c;
}
*{box-sizing:border-box;margin:0;padding:0}
html,body{width:1200px;height:823px;overflow:hidden;background:var(--bg)}
body{position:relative;font-family:"PT Sans",sans-serif;color:var(--body)}

.flyer{position:absolute;top:61px;width:496px;height:704px;background:var(--cream);overflow:hidden;box-shadow:0 4px 14px rgba(0,0,0,.25)}
.flyer--welcome{left:85px}
.flyer--features{left:628px}

.hero{position:absolute;left:0;top:0;width:496px;height:236px;background:var(--white)}
.hero-photo{position:absolute;left:0;top:0;height:236px}
.flyer--welcome .hero-photo{width:300px;background:linear-gradient(90deg,#d9b79a 0%,#e6cdb5 45%,#f3ebe2 80%,rgba(255,255,255,0) 100%)}
.flyer--features .hero-photo{width:496px;background:linear-gradient(100deg,#b48a6a 0%,#d7b28f 30%,#c98a80 55%,#e7a7b7 75%,#9c7b68 100%)}
.hero-waves{position:absolute;left:0;top:206px;width:496px;height:40px}

.wordmark{position:absolute;font-family:"Itim",sans-serif;color:var(--teal);text-align:center;line-height:1}
.wordmark .name{display:block;font-size:33px}
.wordmark .sub{display:block;font-size:14px;letter-spacing:5px;margin-top:4px}
.wordmark-dot{position:absolute;left:50%;top:-26px;width:14px;height:14px;margin-left:-7px;border-radius:50%;background:var(--teal)}
.flyer--welcome .wordmark{left:300px;top:124px;width:190px}
.flyer--features .wordmark{left:148px;top:346px;width:200px}

.tagline{position:absolute;right:4px;top:196px;font-family:"Caveat",cursive;font-size:30px;color:var(--white);transform:rotate(-6deg)}

.welcome-title{position:absolute;left:0;top:264px;width:496px;text-align:center;font-family:"Itim",sans-serif;font-size:25px;color:var(--teal);font-weight:400}
.intro{position:absolute;left:28px;width:440px;text-align:center;font-size:12.4px;line-height:14.2px}
.intro--one{top:297px}
.intro--two{top:371px}
.intro--three{top:439px}

.bird{position:absolute;width:44px;height:52px;border-radius:50% 50% 40% 40%;background:linear-gradient(160deg,#e7a6c8,#c983ac)}
.bird--left{left:14px;top:422px}
.bird--right{left:436px;top:422px}
.washing-line{position:absolute;left:40px;top:456px;width:416px;height:40px}

.snapshot{position:absolute;background:var(--white);padding:8px 8px 22px;box-shadow:0 3px 8px rgba(0,0,0,.22)}
.snapshot .photo{width:100%;height:100%}
.snapshot-peg{position:absolute;top:-8px;left:50%;width:5px;height:14px;margin-left:-2px;background:var(--peg);border-radius:1px}

.enrolling{position:absolute;left:0;top:596px;width:496px;text-align:center;font-family:"Itim",sans-serif;font-size:25px;color:var(--pink)}
.enrolling svg{vertical-align:-2px;margin:0 10px}

.contact-bar{position:absolute;left:0;bottom:0;width:496px;height:67px;background:var(--navy);color:var(--white);text-align:center}
.contact-call{position:absolute;left:0;top:16px;width:496px;font-size:12.4px}
.contact-call .phone{font-family:"Itim",sans-serif;font-size:14px;margin:0 2px}
.contact-call svg{vertical-align:-2px;margin:0 4px 0 12px}
.contact-web{position:absolute;left:0;top:41px;width:496px;font-size:12px}
.contact-web .email{color:#cfe0ff;margin-left:6px}
.contact-web svg{vertical-align:-1px;margin:0 4px 0 0}

.features-list{position:absolute;left:24px;top:408px;width:456px;list-style:none;font-size:10.6px;line-height:12.8px;letter-spacing:-.2px}
.features-list li{position:relative;padding-left:16px;margin-bottom:6px}
.features-list li.plain{margin-top:-2px}
.features-list li svg{position:absolute;left:0;top:1px}
.footnote{position:absolute;left:40px;top:561px;font-size:8px}
.activities{position:absolute;left:0;top:576px;width:496px;text-align:center;font-family:"Itim",sans-serif;font-size:15.5px;color:var(--activity)}
.activities .sep{margin:0 5px;font-size:10px;vertical-align:2px}
</style>
</head>
<body>

<!-- Front side -->
<section class="flyer flyer--welcome">
  <header class="hero">
    <div class="hero-photo" role="img" aria-label="Smiling young girl holding up paint-covered hands"></div>
    <div class="wordmark"><span class="wordmark-dot"></span><span class="name">Bright Acorn</span><span class="sub">DAY NURSERY</span></div>
    <svg class="hero-waves" viewBox="0 0 496 40" aria-hidden="true">
      <path d="M0 6 C120 30 300 34 496 12" fill="none" stroke="var(--teal-line)" stroke-width="1.6"/>
      <path d="M0 14 C150 38 320 36 496 20 L496 40 L0 40 Z" fill="var(--cream)"/>
      <path d="M0 14 C150 38 320 36 496 20" fill="none" stroke="var(--teal-line)" stroke-width="1.6"/>
    </svg>
  </header>

  <h1 class="welcome-title">Welcome to Bright Acorn Day Nursery</h1>
  <p class="intro intro--one">We are a privately owned, vibrant nursery offering your child a caring, family environment within the lovely Wexley Estate in Hollowfield. We offer high quality day care for all children from 3 months to 5 years, treating each child as a treasured individual.</p>
  <p class="intro intro--two">We have a passion for delivering high quality care, love and fun learning opportunities. We provide a loving and nurturing family environment enabling children to experience such homely activities as they would at home both within the setting and also in the local community.</p>
  <p class="intro intro--three">At Bright Acorn we promote<br>confident, happy, caring, collaborative learners!</p>

  <div class="bird bird--left" role="img" aria-label="Pink bird holding the washing line"></div>
  <div class="bird bird--right" role="img" aria-label="Pink bird holding the washing line"></div>
  <svg class="washing-line" viewBox="0 0 416 40" aria-hidden="true">
    <path d="M0 6 Q208 44 416 6" fill="none" stroke="var(--string)" stroke-width="1.4"/>
  </svg>

  <figure class="snapshot" style="left:40px;top:488px;width:122px;height:104px;transform:rotate(-8deg)">
    <span class="snapshot-peg"></span>
    <div class="photo" role="img" aria-label="Play corner with a red puppet theatre" style="background:linear-gradient(135deg,#7a2a1e,#c0392b 50%,#d9a441)"></div>
  </figure>
  <figure class="snapshot" style="left:186px;top:484px;width:120px;height:104px;transform:rotate(2deg)">
    <span class="snapshot-peg"></span>
    <div class="photo" role="img" aria-label="Bright playroom with a small table and soft blocks" style="background:linear-gradient(160deg,#e9e2d6,#c8b79c 60%,#e3c640)"></div>
  </figure>
  <figure class="snapshot" style="left:330px;top:484px;width:132px;height:108px;transform:rotate(7deg)">
    <span class="snapshot-peg"></span>
    <div class="photo" role="img" aria-label="Garden room with toy animals on a green mat" style="background:linear-gradient(150deg,#c9c2b5,#6f8f3a 55%,#d98aa0)"></div>
  </figure>

  <p class="enrolling"><svg width="18" height="16" viewBox="0 0 18 16" aria-hidden="true"><path d="M9 15 C3 10 1 7 1 4.5 A4 4 0 0 1 9 3 A4 4 0 0 1 17 4.5 C17 7 15 10 9 15Z" fill="var(--pink-soft)"/></svg>Now Enrolling<svg width="18" height="16" viewBox="0 0 18 16" aria-hidden="true"><path d="M9 15 C3 10 1 7 1 4.5 A4 4 0 0 1 9 3 A4 4 0 0 1 17 4.5 C17 7 15 10 9 15Z" fill="var(--pink-soft)"/></svg></p>

  <footer class="contact-bar">
    <p class="contact-call">Call us now on <svg width="14" height="12" viewBox="0 0 14 12" aria-hidden="true"><path d="M1 4 Q7 -1 13 4 L11 6 L9 4.5 L5 4.5 L3 6 Z M3 7 H11 V11 H3 Z" fill="var(--white)"/></svg><span class="phone">0208 441 7263</span> for more details or to arrange a visit!</p>
    <p class="contact-web">www.brightacornwexley.co.uk <span class="email">brightacorndaynursery@brightacornwexley.co.uk</span></p>
  </footer>
</section>

<!-- Reverse side -->
<section class="flyer flyer--features">
  <header class="hero">
    <div class="hero-photo" role="img" aria-label="Group of children sitting on the floor pulling funny faces"></div>
    <p class="tagline">Learning Through play</p>
    <svg class="hero-waves" viewBox="0 0 496 40" aria-hidden="true">
      <path d="M0 6 C120 30 300 34 496 12" fill="none" stroke="var(--teal-line)" stroke-width="1.6"/>
      <path d="M0 14 C150 38 320 36 496 20 L496 40 L0 40 Z" fill="var(--cream)"/>
      <path d="M0 14 C150 38 320 36 496 20" fill="none" stroke="var(--teal-line)" stroke-width="1.6"/>
    </svg>
  </header>

  <figure class="snapshot" style="left:12px;top:244px;width:124px;height:112px;transform:rotate(-7deg)">
    <span class="snapshot-peg"></span>
    <div class="photo" role="img" aria-label="Toddler playing at a toy kitchen" style="background:linear-gradient(140deg,#c7473a,#8d2b22 50%,#d9b99a)"></div>
  </figure>
  <figure class="snapshot" style="left:358px;top:248px;width:126px;height:112px;transform:rotate(7deg)">
    <span class="snapshot-peg"></span>
    <div class="photo" role="img" aria-label="Child playing on a patterned rug" style="background:linear-gradient(150deg,#d8d0c4,#8c7b6c 55%,#c9bfb2)"></div>
  </figure>

  <div class="wordmark"><span class="wordmark-dot"></span><span class="name">Bright Acorn</span><span class="sub">DAY NURSERY</span></div>

  <ul class="features-list">
    <li><svg width="11" height="10" viewBox="0 0 11 10" aria-hidden="true"><path d="M1 5 L4 8 L10 1" fill="none" stroke="var(--teal)" stroke-width="2"/></svg>We offer uniquely flexible days and hourly rates.*</li>
    <li class="plain">Our opening hours are 7.45am to 6:15pm. Our convenient location gives plenty of free parking.</li>
    <li><svg width="11" height="10" viewBox="0 0 11 10" aria-hidden="true"><path d="M1 5 L4 8 L10 1" fill="none" stroke="var(--teal)" stroke-width="2"/></svg>ALL 3 and 4 years olds, and eligible 2 year olds, are entitled to up to 15 hours free sessions.</li>
    <li><svg width="11" height="10" viewBox="0 0 11 10" aria-hidden="true"><path d="M1 5 L4 8 L10 1" fill="none" stroke="var(--teal)" stroke-width="2"/></svg>We have playrooms dedicated to each age group, and whatever the weather, your child will be able to play outside in the fresh air within our adventure garden.</li>
    <li><svg width="11" height="10" viewBox="0 0 11 10" aria-hidden="true"><path d="M1 5 L4 8 L10 1" fill="none" stroke="var(--teal)" stroke-width="2"/></svg>Secure Web Cams are installed in each room, giving you a delightful insight into your child's day from wherever you are.</li>
    <li><svg width="11" height="10" viewBox="0 0 11 10" aria-hidden="true"><path d="M1 5 L4 8 L10 1" fill="none" stroke="var(--teal)" stroke-width="2"/></svg>We have a unique and practical app where parents receive alerts and are able to see videos and pictures of their children's day and unique moments.</li>
  </ul>
  <p class="footnote">* Subject to availability</p>

  <p class="activities">Spanish<span class="sep">●</span>Yoga<span class="sep">●</span>Music<span class="sep">●</span>Cooking<span class="sep">●</span>Handsign</p>

  <p class="enrolling"><svg width="18" height="16" viewBox="0 0 18 16" aria-hidden="true"><path d="M9 15 C3 10 1 7 1 4.5 A4 4 0 0 1 9 3 A4 4 0 0 1 17 4.5 C17 7 15 10 9 15Z" fill="var(--pink-soft)"/></svg>Now Enrolling<svg width="18" height="16" viewBox="0 0 18 16" aria-hidden="true"><path d="M9 15 C3 10 1 7 1 4.5 A4 4 0 0 1 9 3 A4 4 0 0 1 17 4.5 C17 7 15 10 9 15Z" fill="var(--pink-soft)"/></svg></p>

  <footer class="contact-bar">
    <p class="contact-call">Call us now on <svg width="14" height="12" viewBox="0 0 14 12" aria-hidden="true"><path d="M1 4 Q7 -1 13 4 L11 6 L9 4.5 L5 4.5 L3 6 Z M3 7 H11 V11 H3 Z" fill="var(--white)"/></svg><span class="phone">0208 441 7263</span> for more details or to arrange a visit!</p>
    <p class="contact-web"><svg width="8" height="11" viewBox="0 0 8 11" aria-hidden="true"><path d="M4 11 C1 6 0 5 0 4 A4 4 0 0 1 8 4 C8 5 7 6 4 11Z M4 2.5 A1.5 1.5 0 1 0 4 5.5 A1.5 1.5 0 1 0 4 2.5Z" fill="#cfe0ff" fill-rule="evenodd"/></svg><span class="email" style="margin-left:0">87 Hazelmere road SE6 4PW</span></p>
  </footer>
</section>

</body>
</html>
```